Stationery Design Project for Marketing Consultancy

I have started a new consultancy business and require the following elements to be designed using existing logo:
• Business card
• Letterhead
• Envelope (DL, C4, C5)
• Microsoft word template for report writing
• A4 Presentation Folder
• Powerpoint template
COPY FOR FRONT AND BACK OF BUSINESS CARD
logo
'Countable Growth. Bold Outcomes' slogan (but no need to use existing lockup with logo)
name, B Bus. Mktg, Grad Dip Digital Mktg, CPM (post nominal abbreviations in smaller font)
mobile: 04XX-XXX-XXX (I will give details to the winner to add)
website: www.quorvale.com.au
email: info@quorvale.com.au
COPY FOR LETTERHEAD
Logo
Company Name
Please, submit your designs that include business card, letterhead and envelope. Once selected the winner will be asked to complete the project by creating the rest of the artwork.
FINAL FILES
Print ready files to be supplied as well as Indesign files so that minor amends can be made if necessary in future.
• Layered vectors in EPS & PDF
• Screen quality JPEG & PNGs
ABOUT THE BUSINESS: QUORVALE
I work with clients to understand their business challenges, developing and executing measurable marketing strategies tied to key business metrics. Services include:
Services include:
• Business planning and business development
• Marketing and brand strategy
• Insight-driven integrated campaigns
• Loyalty programs and retention marketing
• Marketing automation
• Direct marketing (traditional and digital)
• Content strategy and development
Hi everyone,
Target Market(s)
Corporate decision makers (heads of marketing, general managers etc) and small to medium sized business owners. Predominately male aged 35+
Industry/Entity Type
Marketing
Requirements
Must have
- BRAND PERSONALITY
The successful design will communicate brand personality. I am a professional, results-driven entrepreneur, but want to show off my creative flair.
MEMORABILITY
Looking for a unique and eye-catching design. Am considering special printing effects (die cuts, letterpress, interactive elements, embossing, foiling etc) or a striking minimalist approach.
Nice to have
- I have a mission that could be incorporated on reverse if room -
Turning insights into actions & passion into profit.
Should not have
- Use of pink or green.

```html
<!DOCTYPE html>
<html lang="en">
<head>
<meta charset="utf-8">
<title>Quorvale Business Card</title>
<link href="https://fonts.googleapis.com/css2?family=Open+Sans:wght@300;400;700;800&display=swap" rel="stylesheet">
<style>
  :root {
    --backdrop: #2f2a29;
    --paper: #edece8;
    --ink: #2a2a2a;
    --ink-soft: #4a4a4a;
    --rule: #6b6b6b;
  }
  html, body {
    margin: 0;
    padding: 0;
    width: 1200px;
    height: 901px;
    overflow: hidden;
    background: var(--backdrop);
    font-family: "Open Sans", Arial, sans-serif;
  }
  .stage {
    position: relative;
    width: 1200px;
    height: 901px;
    display: flex;
    align-items: center;
    justify-content: center;
    gap: 60px;
  }
  .card {
    position: relative;
    width: 510px;
    height: 300px;
    background: var(--paper);
    color: var(--ink);
    box-shadow: 0 10px 28px rgba(0,0,0,0.45);
    box-sizing: border-box;
  }
  /* Front */
  .card--front {
    display: flex;
    flex-direction: column;
    align-items: center;
    justify-content: center;
  }
  .brand {
    display: flex;
    align-items: center;
    gap: 14px;
  }
  .brand__mark {
    width: 46px;
    height: 46px;
    border-radius: 50%;
    background: var(--ink);
  }
  .brand__name {
    font-weight: 800;
    font-size: 54px;
    letter-spacing: 1px;
    line-height: 1;
    color: var(--ink);
  }
  .slogan {
    margin-top: 10px;
    font-weight: 700;
    font-size: 14.5px;
    letter-spacing: 0.6px;
    text-transform: uppercase;
    color: var(--ink);
  }
  /* Back */
  .card--back {
    padding: 34px 40px;
  }
  .card--back .brand {
    position: absolute;
    top: 34px;
    right: 40px;
    gap: 8px;
  }
  .card--back .brand__mark {
    width: 22px;
    height: 22px;
  }
  .card--back .brand__name {
    font-size: 24px;
  }
  .person {
    margin-top: 78px;
    padding-bottom: 14px;
    border-bottom: 1px solid var(--rule);
    width: 260px;
  }
  .person__name {
    font-weight: 300;
    font-size: 28px;
    line-height: 1.1;
    color: var(--ink);
  }
  .person__credentials {
    margin-top: 6px;
    font-weight: 300;
    font-size: 13px;
    line-height: 1.45;
    color: var(--ink-soft);
  }
  .contact {
    margin-top: 14px;
    font-weight: 300;
    font-size: 13px;
    line-height: 1.6;
    color: var(--ink-soft);
  }
  .contact p { margin: 0; }
</style>
</head>
<body>
  <main class="stage">
    <section class="card card--front" aria-label="Business card front">
      <div class="brand">
        <span class="brand__name">QUORVALE</span>
        <span class="brand__mark" aria-hidden="true"></span>
      </div>
      <p class="slogan">Countable Growth. Bold Outcomes.</p>
    </section>

    <section class="card card--back" aria-label="Business card back">
      <div class="brand">
        <span class="brand__name">QUORVALE</span>
        <span class="brand__mark" aria-hidden="true"></span>
      </div>
      <div class="person">
        <div class="person__name">Nora Whitfield</div>
        <div class="person__credentials">B Bus. Mktg,<br>Grad Dip Digital Mktg, CPM</div>
      </div>
      <div class="contact">
        <p>04XX-XXX-XXX</p>
        <p>info@quorvale.com.au</p>
        <p>www.quorvale.com.au</p>
      </div>
    </section>
  </main>
</body>
</html>
```